2in1 Bartender & Sommelier needs a business card

I need a business card. I worked as a bartender in many places but I just finished a sommelier school and I would like a new business card. I like minimal design, natural materials and something what makes the people think :) I try to be creative in cocktail making, like little mixology, little twist on recipes... I like to travel and discover new places, cultures and of course interesting drinks and improve continously...live a little bit crazy life. And I like what I do...

Target Market(s)

restaurant/winebar managers, winemakers, other sommeliers and bartenders, people who work in food and beverage sector

Industry/Entity Type

Hospitality

Contact Information for Business Card

Rozsa Tarkany
Bartender & Sommelier
Phone: (FR) +33 6 4827 3190
(HU) +36 70 918 6352

Font styles to use
Script

Requirements
Must have
• Some sign, I am a bartender and sommelier as well.
Nice to have
• black and white maybe with 1 or 2 extra color
Should not have
• very colourful, to many things on the card

```html
<!DOCTYPE html>
<html lang="en">
<head>
<meta charset="utf-8">
<title>Rozsa Tarkany – Business Card</title>
<link rel="stylesheet" href="https://fonts.googleapis.com/css2?family=Allura&family=Open+Sans:wght@400&display=swap">
<style>
  :root {
    --backdrop: #e6e6e4;
    --card: #ffffff;
    --panel: #3d3d3d;
    --emblem: #4b4b4b;
    --name: #8a8a8a;
    --title: #5f5f5f;
    --rule: #9a9a9a;
    --contact: #8a8a8a;
    --icon: #8f8f8f;
  }
  html, body {
    margin: 0;
    width: 1200px;
    height: 1000px;
    overflow: hidden;
    background: var(--backdrop);
  }
  .canvas {
    position: relative;
    width: 1200px;
    height: 1000px;
  }
  .business-card {
    position: absolute;
    left: 203px;
    top: 262px;
    width: 794px;
    height: 476px;
    background: var(--card);
    overflow: hidden;
  }
  .side-panel {
    position: absolute;
    left: 0;
    top: 0;
  }
  .emblem {
    position: absolute;
    left: 77px;
    top: 99px;
    width: 90px;
    height: 275px;
    background: var(--emblem);
    border-radius: 4px;
  }
  .holder-name {
    position: absolute;
    left: 300px;
    width: 410px;
    top: 100px;
    margin: 0;
    text-align: center;
    font-family: "Allura", cursive;
    font-weight: 400;
    font-size: 62px;
    line-height: 1;
    color: var(--name);
  }
  .holder-role {
    position: absolute;
    left: 300px;
    width: 412px;
    top: 201px;
    margin: 0;
    text-align: center;
    font-family: "Open Sans", sans-serif;
    font-size: 20px;
    letter-spacing: 3.4px;
    color: var(--title);
  }
  .divider {
    position: absolute;
    left: 300px;
    top: 263px;
    width: 404px;
    height: 2px;
    background: var(--rule);
  }
  .contact {
    position: absolute;
    left: 350px;
    top: 307px;
    display: flex;
    align-items: center;
    gap: 22px;
  }
  .contact-icon {
    width: 30px;
    height: 30px;
    flex: none;
  }
  .phone-list {
    margin: 0;
    padding: 0;
    list-style: none;
    font-family: "Open Sans", sans-serif;
    font-size: 18px;
    line-height: 28px;
    color: var(--contact);
  }
</style>
</head>
<body>
<main class="canvas">
  <article class="business-card">
    <svg class="side-panel" width="300" height="476" viewBox="0 0 300 476" aria-hidden="true">
      <path d="M0 0 H194 Q379.5 238 191 476 H0 Z" fill="var(--panel)"/>
    </svg>
    <div class="emblem" role="img" aria-label="Line emblem of a wine glass with a swirling stroke rising from the bowl"></div>

    <h1 class="holder-name">Rozsa Tarkany</h1>
    <p class="holder-role">Bartender &amp; Sommelier</p>
    <div class="divider"></div>

    <div class="contact">
      <svg class="contact-icon" viewBox="0 0 30 30" aria-hidden="true">
        <circle cx="15" cy="15" r="15" fill="var(--icon)"/>
        <path d="M11.2 8.2c.6-.4 1.3-.2 1.6.4l1.2 2.4c.3.6.1 1.2-.4 1.6l-1 .7c.7 1.6 1.9 2.9 3.5 3.7l.8-.9c.4-.5 1.1-.6 1.6-.3l2.3 1.4c.6.4.7 1.1.3 1.7l-.9 1.2c-.6.8-1.7 1.1-2.7.7-3.9-1.5-6.8-4.5-8.2-8.4-.3-1 0-2 .8-2.6z" fill="#ffffff"/>
      </svg>
      <ul class="phone-list">
        <li>(FR) +33 6 4827 3190</li>
        <li>(HU) +36 70 918 6352</li>
      </ul>
    </div>
  </article>
</main>
</body>
</html>
```